TV Antenna Installation business needs a unique flyer

We need a simple but effective flyer design for our TV Aerial installation company based in Newcastle, NSW, Australia called Bright Wave TV & Aerial Svcs.
We are trying to target areas where there has been a new transmitter installed and most houses just require their aerial redirecting and tv's retuning.

Industry/Entity Type

Business

Requirements
Must have
• We would like the idea of a headline phrase such as " Poor TV reception……..now a thing from the past" or something similar & catchy.
Also "Did you know a new transmitter has been recently installed in your area, we can therefore now GUARANTEE 100% PERFECT PICTURE
Charges from only $95.
- Free 5 year warranty
- Free signal testing
- Free Onsite Quote
Phone 0412 736 205
Nice to have
• Other services include:

- New Installs
- Extra Points & repairs
- TV wall mounting/Home Cinema
- Pull down tall masts

Modern tv picture, see example uploaded

```html
<!DOCTYPE html>
<html lang="en">
<head>
<meta charset="utf-8">
<title>Bright Wave TV &amp; Aerial Svcs – Flyer</title>
<link rel="stylesheet" href="https://fonts.googleapis.com/css2?family=Bree+Serif&family=Open+Sans:ital,wght@0,600;0,700;1,400&family=Questrial&display=swap">
<style>
  :root {
    --orange: #f7821e;
    --green: #55e64c;
    --green-text: #4ccc46;
    --white: #ffffff;
    --frame: #1a1a1a;
  }
  * { margin: 0; padding: 0; box-sizing: border-box; }
  html, body { width: 1200px; height: 874px; overflow: hidden; background: var(--white); }
  .flyer { position: relative; width: 1200px; height: 874px; background: var(--white); font-family: "Open Sans", sans-serif; }

  .phone { position: absolute; left: 36px; top: 38px; display: flex; align-items: center; gap: 8px; }
  .phone svg { width: 46px; height: 46px; }
  .phone-number { font-family: "Open Sans", sans-serif; font-weight: 700; font-size: 52px; color: var(--orange); letter-spacing: 0.5px; line-height: 1; }

  .brand { position: absolute; right: 26px; top: 30px; display: flex; align-items: center; gap: 14px; }
  .brand-mark { width: 22px; height: 22px; border-radius: 50%; background: var(--green); }
  .brand-name { font-family: "Bree Serif", serif; font-size: 58px; color: var(--orange); line-height: 1; }

  .photos { position: absolute; left: 12px; top: 127px; display: flex; gap: 5px; }
  .photo { width: 291px; height: 300px; border: 3px solid var(--frame); }
  .photo-dish { background: linear-gradient(135deg, #8a6a5a 0%, #b9bfc8 45%, #2b3e7a 100%); }
  .photo-remote { background: radial-gradient(circle at 60% 55%, #9aa3ad 0%, #6f7f93 40%, #c74a5a 100%); }
  .photo-cables { background: linear-gradient(160deg, #f2f2f2 0%, #c9a24a 40%, #1f2a3a 75%, #e9e9e9 100%); }
  .photo-antenna { background: linear-gradient(180deg, #6f9fd6 0%, #b7d0ea 60%, #8b4a32 100%); }

  .accent-line { position: absolute; left: 0; top: 432px; width: 1200px; height: 18px; background: var(--green); }
  .banner { position: absolute; left: 0; top: 450px; width: 1200px; height: 185px; background: var(--orange); color: var(--white); padding: 0 0 0 58px; }
  .headline { font-family: "Bree Serif", serif; font-size: 50px; line-height: 1; margin-top: 21px; }
  .intro { font-family: "Questrial", sans-serif; font-size: 30px; line-height: 40px; margin-top: 16px; }
  .intro strong { font-weight: 400; font-size: 33px; }

  .offer-bars { position: absolute; left: 0; top: 640px; width: 1200px; height: 52px; }
  .offer-title { position: absolute; top: 645px; font-family: "Open Sans", sans-serif; font-weight: 700; font-size: 32px; color: var(--white); line-height: 42px; }
  .offer-title-left { left: 94px; }
  .offer-title-right { left: 688px; }

  .checklist { position: absolute; top: 698px; list-style: none; }
  .checklist-left { left: 100px; }
  .checklist-right { left: 670px; }
  .checklist li { display: flex; align-items: center; gap: 14px; height: 42px; font-style: italic; font-size: 29px; color: var(--green-text); }
  .checklist svg { width: 26px; height: 26px; flex: none; }
</style>
</head>
<body>
<main class="flyer">
  <div class="phone">
    <svg viewBox="0 0 46 46" aria-hidden="true">
      <circle cx="23" cy="23" r="20" fill="none" stroke="var(--green)" stroke-width="3"/>
      <path d="M17 12c1.5-1 3-1 3.6 0.3l2 4c.4.9 0 1.7-.8 2.3l-1.5 1c.6 2.8 2.6 5.2 5 6.6l1.3-1.2c.7-.6 1.6-.7 2.3-.1l3.6 2.6c1 .7.9 2.2-.1 3.4-2 2.2-4.6 2.4-7.3.8-5-3-8.7-8.5-9.6-13.8-.4-2.5.2-4.6 1.5-5.9z" fill="var(--green)"/>
    </svg>
    <span class="phone-number">0412 736 205</span>
  </div>

  <div class="brand">
    <span class="brand-mark"></span>
    <span class="brand-name">Bright Wave</span>
  </div>

  <section class="photos">
    <div class="photo photo-dish" role="img" aria-label="Technician fitting a satellite dish to a wall"></div>
    <div class="photo photo-remote" role="img" aria-label="TV remote control in front of a screen"></div>
    <div class="photo photo-cables" role="img" aria-label="Hand holding a bundle of coaxial cable connectors"></div>
    <div class="photo photo-antenna" role="img" aria-label="Installer on a roof adjusting a TV antenna"></div>
  </section>

  <div class="accent-line"></div>
  <section class="banner">
    <h1 class="headline">Poor TV reception........now a thing from the past</h1>
    <p class="intro">Did you know a new transmitter has been recently installed in your area, we<br>can therefore now <strong>GUARANTEE 100% PERFECT PICTURE</strong></p>
  </section>

  <svg class="offer-bars" viewBox="0 0 1200 52" preserveAspectRatio="none" aria-hidden="true">
    <polygon points="0,0 628,0 590,52 0,52" fill="var(--green)"/>
    <polygon points="650,0 1200,0 1200,52 612,52" fill="var(--green)"/>
  </svg>
  <h2 class="offer-title offer-title-left">Charges from only $95</h2>
  <h2 class="offer-title offer-title-right">Other services include</h2>

  <ul class="checklist checklist-left">
    <li><svg viewBox="0 0 26 26" aria-hidden="true"><rect x="2" y="7" width="16" height="16" fill="none" stroke="var(--orange)" stroke-width="2.5"/><path d="M6 14l5 5L24 3" fill="none" stroke="var(--orange)" stroke-width="3"/></svg>Free 5 years warranty</li>
    <li><svg viewBox="0 0 26 26" aria-hidden="true"><rect x="2" y="7" width="16" height="16" fill="none" stroke="var(--orange)" stroke-width="2.5"/><path d="M6 14l5 5L24 3" fill="none" stroke="var(--orange)" stroke-width="3"/></svg>Free signal testing</li>
    <li><svg viewBox="0 0 26 26" aria-hidden="true"><rect x="2" y="7" width="16" height="16" fill="none" stroke="var(--orange)" stroke-width="2.5"/><path d="M6 14l5 5L24 3" fill="none" stroke="var(--orange)" stroke-width="3"/></svg>Free Onsite Quote</li>
  </ul>

  <ul class="checklist checklist-right">
    <li><svg viewBox="0 0 26 26" aria-hidden="true"><rect x="2" y="7" width="16" height="16" fill="none" stroke="var(--orange)" stroke-width="2.5"/><path d="M6 14l5 5L24 3" fill="none" stroke="var(--orange)" stroke-width="3"/></svg>New Installs</li>
    <li><svg viewBox="0 0 26 26" aria-hidden="true"><rect x="2" y="7" width="16" height="16" fill="none" stroke="var(--orange)" stroke-width="2.5"/><path d="M6 14l5 5L24 3" fill="none" stroke="var(--orange)" stroke-width="3"/></svg>Extra Points &amp; repairs</li>
    <li><svg viewBox="0 0 26 26" aria-hidden="true"><rect x="2" y="7" width="16" height="16" fill="none" stroke="var(--orange)" stroke-width="2.5"/><path d="M6 14l5 5L24 3" fill="none" stroke="var(--orange)" stroke-width="3"/></svg>TV wall mounting/Home Cinema</li>
    <li><svg viewBox="0 0 26 26" aria-hidden="true"><rect x="2" y="7" width="16" height="16" fill="none" stroke="var(--orange)" stroke-width="2.5"/><path d="M6 14l5 5L24 3" fill="none" stroke="var(--orange)" stroke-width="3"/></svg>Pull down tall masts</li>
  </ul>
</main>
</body>
</html>
```